Quorvane Capital Modern Business Card

We need a modern business card template designed for Quorvane Capital.
Quorvane Capital is a diversified global cryptocurrency investment fund.

The font under the logo: Hiragino Kaku Gothic Pro

Color Hexcode: Main colors white (ffffff) & teal (188383), we are open to adding #fcca46 as an accent

Target Market(s)

Accredited Investors, high net worth individuals and institutional investors

Industry/Entity Type

Investment

Contact Information for Business Card

Contact Information should contain
Name
main phone +1 720 555 0147
cell
email

Font styles to use
Sans Serif
Other font styles liked:
• Hiragino Kaku Gothic Pro

Requirements
Must have
• would like to have icons that identify the contact information
• include our website: www.quorvanecapital.example
• include our Tagline: Diversified Crypto Investment Funds
Nice to have
• Would like to have a simple back side with the logo (without the words) and plenty of space

```html
<!DOCTYPE html>
<html lang="en">
<head>
<meta charset="utf-8">
<title>Quorvane Capital – Business Card</title>
<link rel="stylesheet" href="https://fonts.googleapis.com/css2?family=Montserrat:wght@300;400&family=Poppins:wght@300;400&display=swap">
<style>
  :root{
    --teal-green:#35c391;
    --mint:#d6f2e8;
    --navy:#2b5a72;
    --lock-yellow:#ecc83e;
    --lock-yellow-light:#f6d85a;
    --cream:#fbf3d8;
    --silver-top:#f4f4f5;
    --silver-bottom:#d9dadc;
    --ink:#1a1a1a;
  }
  *{margin:0;padding:0;box-sizing:border-box;}
  html,body{width:1200px;height:720px;overflow:hidden;background:#fff;}
  .card{position:relative;width:1200px;height:720px;background:var(--teal-green);overflow:hidden;font-family:"Poppins",sans-serif;}

  .band{position:absolute;background:var(--mint);}
  .band--header{left:0;top:64px;width:1200px;height:130px;}
  .band--tagline{left:0;top:397px;width:509px;height:129px;}

  .brand-tab{position:absolute;left:75px;top:-40px;width:220px;height:303px;border-radius:0 0 110px 110px;
    background:linear-gradient(180deg,var(--silver-top),var(--silver-bottom));
    display:flex;flex-direction:column;align-items:center;justify-content:flex-end;padding-bottom:72px;}
  .brand-dot{width:56px;height:56px;border-radius:50%;background:var(--teal-green);margin-bottom:22px;}
  .brand-name{font-family:"Poppins",sans-serif;font-weight:400;font-size:17px;color:var(--ink);letter-spacing:.2px;}

  .person{position:absolute;left:310px;top:64px;color:var(--navy);font-family:"Montserrat",sans-serif;}
  .person-name{font-family:inherit;font-weight:300;font-size:94px;line-height:1;letter-spacing:2px;}
  .person-role{font-weight:300;font-size:36px;line-height:1;margin-top:2px;}

  .tagline{position:absolute;left:72px;top:420px;font-weight:300;font-size:41px;line-height:43px;color:var(--ink);}

  .lock-art{position:absolute;left:509px;top:211px;width:700px;height:520px;border-radius:44px 44px 0 0;
    background:linear-gradient(180deg,var(--lock-yellow-light) 0%,var(--lock-yellow) 26%,var(--lock-yellow) 100%);}

  .contact-list{position:absolute;right:0;top:331px;display:flex;flex-direction:column;align-items:flex-end;gap:13px;list-style:none;}
  .contact{display:flex;align-items:center;height:60px;}
  .contact-icon{width:36px;height:36px;margin-right:10px;flex:none;}
  .contact-text{height:60px;display:flex;align-items:center;background:var(--cream);
    padding:0 26px 0 13px;font-size:20px;color:var(--navy);font-weight:400;white-space:nowrap;}
</style>
</head>
<body>
<main class="card">
  <div class="band band--header"></div>
  <div class="band band--tagline"></div>

  <div class="lock-art" role="img" aria-label="Illustration of a large yellow padlock symbolising secure investment"></div>

  <div class="brand-tab">
    <span class="brand-dot"></span>
    <span class="brand-name">QUORVANE CAPITAL</span>
  </div>

  <div class="person">
    <h1 class="person-name">ELENA MARSH</h1>
    <p class="person-role">CEO</p>
  </div>

  <p class="tagline">Diversified Crypto<br>Investment Funds</p>

  <ul class="contact-list">
    <li class="contact contact--phone">
      <svg class="contact-icon" viewBox="0 0 38 38" aria-hidden="true">
        <rect x="10" y="2" width="18" height="34" rx="3" fill="#2b5a72"/>
        <rect x="12.5" y="6" width="13" height="24" rx="1" fill="#3f7f9c"/>
        <circle cx="19" cy="33" r="1.4" fill="#9fc3d3"/>
      </svg>
      <span class="contact-text">+1 720 555 0147</span>
    </li>
    <li class="contact contact--email">
      <svg class="contact-icon" viewBox="0 0 38 38" aria-hidden="true">
        <rect x="3" y="12" width="32" height="22" rx="2" fill="#e5b93a" stroke="#2b5a72" stroke-width="1.2"/>
        <rect x="8" y="5" width="22" height="16" fill="#fff" stroke="#cfd6da"/>
        <path d="M3 12 L19 25 L35 12" fill="none" stroke="#2b5a72" stroke-width="1.2"/>
      </svg>
      <span class="contact-text">info@quorvanecapital.example</span>
    </li>
    <li class="contact contact--web">
      <svg class="contact-icon" viewBox="0 0 38 38" aria-hidden="true">
        <rect x="3" y="4" width="32" height="30" rx="2" fill="#2b5a72"/>
        <rect x="6" y="9" width="26" height="22" fill="#1d3e50"/>
        <path d="M9 14h10M9 19h16M9 24h8" stroke="#6fd3a8" stroke-width="2"/>
      </svg>
      <span class="contact-text">quorvanecapital.example</span>
    </li>
    <li class="contact contact--address">
      <svg class="contact-icon" viewBox="0 0 38 38" aria-hidden="true">
        <path d="M3 12 L13 9 L25 12 L35 9 V33 L25 36 L13 33 L3 36 Z" fill="#f1dc8a" stroke="#2b5a72" stroke-width="1"/>
        <path d="M24 3a6 6 0 0 0-6 6c0 5 6 11 6 11s6-6 6-11a6 6 0 0 0-6-6z" fill="#e0463d"/>
        <circle cx="24" cy="9" r="2.2" fill="#fff"/>
      </svg>
      <span class="contact-text">London, Harrow Lane, Nr 08</span>
    </li>
  </ul>
</main>
</body>
</html>
```